Home page design for dealership

Client is a truck dealership out of Dallas that wants a rustic/vintage design-themed website. Prefers to have vintage design details over the use of cowboy or western images, and so, is open to the use of different color schemes.
The focus of the website must be the inventory, with a large centerpiece image about 950 x 400 pixels. The centerpiece becomes a rotating slideshow, in the next stage of ‘buildout’, with a coded website.
Need 3 ‘button’ graphics that will link and include a hover effect.

Dealership info:
Halloway Autos
48217 Brindle Avenue
Kestral, TX 75390
972-438-2917

We need a website design that follows this layout:
-Background - wood panels
-Accent Colors - open to any scheme
-Banner - 950 pixels wide – includes dealer name and phone number with PX, Chirply and Orbix+ icons
-Navigation/Menu Bar – tabs – Home | Inventory | Finance | Vehicle Finder | About Us | Contact Us
-Centerpiece image – 950 x 400 pixels – any newer model truck
-Call-to-action buttons – use your judgment for placement, show the hover effect on one ‘button’
View Our Inventory
Find your Dream Truck
Finance your Truck
-Content section - will include a column for dealer address and hours, and a second column for ‘Welcome to Halloway Autos’ copy(attached). Also needs to accommodate the following logos: Vetrolog, QTR A+, Zumo
Hours: Mon-Fri: 9a – 6p, Sat-Sun: 12p – 6p
-Featured Inventory – row of thumbnails that preview client’s inventory

Below are a few example sites of what client likes:
http://www.1932ginhaus.com/ - likes the clean look of the wood background
http://lunvatorikka.net/ - likes the simple look of paper against wood
https://pampaloma.com/ - Likes the burnt edges effect on the paper background
Updates

This dealership sells pickup trucks. For example: Borland K240, Marven Q38, Tavola Ridgeman. For the centerpiece image, please use a newer model from the examples provided.

```html
<!DOCTYPE html>
<html lang="en">
<head>
<meta charset="utf-8">
<title>Halloway Autos</title>
<link rel="stylesheet" href="https://fonts.googleapis.com/css2?family=Delius&family=Ubuntu:wght@400;500&display=swap">
<style>
  :root {
    --accent: #f7802a;
    --accent-soft: #fb9239;
    --nav-bg: #2c2c2c;
    --nav-line: #3d3d3d;
    --stage: #000000;
    --tab: #2a2a2a;
    --text-light: #ffffff;
    --text-muted: #e6e6e6;
    --input-frame: #333333;
    --placeholder: #8a8a8a;
    --wood-dark: #3b2617;
    --wood-mid: #5a3a22;
    --wood-light: #6e4a2c;
    --wood-seam: #24170d;
  }
  * { box-sizing: border-box; margin: 0; padding: 0; }
  html, body { width: 1200px; height: 485px; overflow: hidden; background: var(--wood-dark); }
  .canvas {
    position: relative;
    width: 1200px;
    height: 485px;
    overflow: hidden;
    font-family: "Ubuntu", sans-serif;
  }
  .wood-panels {
    position: absolute; inset: 0;
    background:
      radial-gradient(ellipse at 50% 40%, transparent 40%, rgba(0,0,0,0.55) 100%),
      repeating-linear-gradient(90deg,
        var(--wood-seam) 0px, var(--wood-seam) 3px,
        var(--wood-mid) 3px, var(--wood-light) 60px, var(--wood-mid) 100px,
        var(--wood-dark) 150px);
  }
  .brand {
    position: absolute; left: 157px; top: 45px;
    width: 224px; height: 62px;
    background: var(--accent);
    display: flex; align-items: center; justify-content: center;
    box-shadow: 0 2px 6px rgba(0,0,0,0.5);
  }
  .brand-name {
    font-family: "Delius", sans-serif;
    font-size: 27px;
    color: var(--text-light);
    white-space: nowrap;
  }
  .phone {
    position: absolute; left: 400px; top: 64px;
    font-family: "Delius", sans-serif;
    font-size: 20px;
    color: var(--text-light);
    display: flex; align-items: center; gap: 8px;
    text-shadow: 0 1px 3px rgba(0,0,0,0.6);
  }
  .phone svg { width: 18px; height: 18px; fill: var(--accent); }
  .search {
    position: absolute; left: 813px; top: 63px;
    width: 239px; height: 32px;
    background: var(--text-light);
    border: 5px solid var(--input-frame);
    padding-left: 8px;
    display: flex; align-items: center;
    font-size: 10px; color: var(--placeholder);
  }
  .side-tabs { position: absolute; left: 1174px; top: 63px; width: 26px; }
  .side-tab { width: 26px; height: 34px; margin-bottom: 1px; background: var(--tab); }
  .side-tab-lone { position: absolute; left: 1174px; top: 417px; width: 26px; height: 34px; background: var(--tab); }
  .nav {
    position: absolute; left: 157px; top: 122px;
    width: 895px; height: 52px;
    background: var(--nav-bg);
  }
  .nav-item {
    position: absolute; top: 0; height: 52px;
    border-right: 1px solid var(--nav-line);
    padding: 13px 0 0 15px;
  }
  .nav-title {
    display: block;
    font-size: 10px; font-weight: 500;
    color: var(--text-light);
    letter-spacing: 0.1px;
    text-transform: uppercase;
    white-space: nowrap;
  }
  .nav-sub {
    display: block; margin-top: 6px;
    font-size: 9px; color: var(--text-muted);
    white-space: nowrap;
  }
  .nav-item.is-active .nav-title { color: var(--accent); }
  .account {
    position: absolute; right: 15px; top: 22px;
    font-size: 10px; font-weight: 500;
    color: var(--text-light);
    text-transform: uppercase;
    display: flex; gap: 10px;
  }
  .stage {
    position: absolute; left: 157px; top: 174px;
    width: 895px; height: 311px;
    background: var(--stage);
  }
  .showcase {
    position: absolute; left: 15px; top: 12px;
    width: 772px; height: 299px;
    background: linear-gradient(180deg, #c9ccce 0%, #9ea3a6 40%, #3a2f33 62%, #6b8a4e 85%, #aeb2b3 100%);
  }
  .cta-list {
    position: absolute; left: 800px; top: 14px;
    width: 84px;
    display: flex; flex-direction: column; gap: 8px;
  }
  .cta {
    display: flex; align-items: center; justify-content: center;
    height: 44px; padding: 0 6px;
    background: var(--tab);
    border: 1px solid var(--nav-line);
    color: var(--text-light);
    font-size: 10px; font-weight: 500;
    line-height: 1.25;
    text-align: center;
    text-transform: uppercase;
    text-decoration: none;
  }
  .cta.is-hover { background: var(--accent-soft); border-color: var(--accent-soft); }
</style>
</head>
<body>
<div class="canvas">
  <div class="wood-panels"></div>

  <div class="brand"><span class="brand-name">Halloway Autos</span></div>

  <div class="phone">
    <svg viewBox="0 0 24 24" aria-hidden="true"><path d="M6.6 10.8a15.1 15.1 0 0 0 6.6 6.6l2.2-2.2a1 1 0 0 1 1-.25 11.4 11.4 0 0 0 3.6.57 1 1 0 0 1 1 1V20a1 1 0 0 1-1 1A17 17 0 0 1 3 4a1 1 0 0 1 1-1h3.5a1 1 0 0 1 1 1c0 1.25.2 2.45.57 3.6a1 1 0 0 1-.25 1z"/></svg>
    <span>972-438-2917</span>
  </div>

  <div class="search">Search...</div>

  <div class="side-tabs">
    <div class="side-tab"></div>
    <div class="side-tab"></div>
    <div class="side-tab"></div>
    <div class="side-tab"></div>
  </div>
  <div class="side-tab-lone"></div>

  <nav class="nav">
    <div class="nav-item is-active" style="left:0;width:86px;">
      <span class="nav-title">Home</span><span class="nav-sub">Return Home</span>
    </div>
    <div class="nav-item" style="left:86px;width:110px;">
      <span class="nav-title">Inventory</span><span class="nav-sub">Responsive Layout</span>
    </div>
    <div class="nav-item" style="left:196px;width:110px;">
      <span class="nav-title">Finance</span><span class="nav-sub">Tools and Modules</span>
    </div>
    <div class="nav-item" style="left:306px;width:120px;">
      <span class="nav-title">Vehicle Finder</span><span class="nav-sub">What's Included</span>
    </div>
    <div class="nav-item" style="left:426px;width:100px;">
      <span class="nav-title">About Us</span><span class="nav-sub">Our Story</span>
    </div>
    <div class="nav-item" style="left:526px;width:106px;">
      <span class="nav-title">Contact Us</span><span class="nav-sub">Find Help Here</span>
    </div>
    <div class="account"><span>Login</span><span>Register</span></div>
  </nav>

  <section class="stage">
    <div class="showcase" role="img" aria-label="Newer model pickup truck parked under a cloudy sky"></div>
    <div class="cta-list">
      <a class="cta is-hover" href="#">View Our Inventory</a>
      <a class="cta" href="#">Find Your Dream Truck</a>
      <a class="cta" href="#">Finance Your Truck</a>
    </div>
  </section>
</div>
</body>
</html>
```